Real Estate Agent Post Card

I am a Realtor that uses direct mail. I am interested in seasonal post cards. I have attached an old spring card (front and back) that was designed by someone else. The front should be spring themed. The return address label is incorrect. I would like to lose that and go with a simple font "Carl Whitby 7 Larkmoor Ct Ste 240 Southgate Mi 48195". I like the language on the back as is.

Target Market(s)

Home Sellers

Industry/Entity Type

Real Estate Agent

Requirements
Must have
• See attached files
Nice to have
• Seasonal photo/art

```html
<!DOCTYPE html>
<html lang="en">
<head>
<meta charset="utf-8">
<title>Spring Listing Postcard – Carl Whitby</title>
<link rel="stylesheet" href="https://fonts.googleapis.com/css2?family=Great+Vibes&family=PT+Sans+Narrow:wght@400;700&family=Source+Sans+3:wght@400;600;700&display=swap">
<style>
  :root {
    --stage: #e9e4dc;
    --cream: #fbefc8;
    --white: #ffffff;
    --plum: #8b3a97;
    --violet-soft: #b79ad8;
    --lilac: #d9c6ee;
    --dash-blue: #3446a9;
    --brand-blue: #1c3bbd;
    --ink: #1d1d1d;
    --sky: #e6eef3;
    --field: #efd2ec;
    --stamp: #9a9a9a;
  }
  * { box-sizing: border-box; margin: 0; padding: 0; }
  html, body { width: 1200px; height: 528px; overflow: hidden; }
  body { background: var(--stage); position: relative; font-family: "Source Sans 3", sans-serif; color: var(--ink); }

  .card { position: absolute; top: 43px; height: 447px; overflow: hidden; box-shadow: 0 2px 6px rgba(0,0,0,.18); }

  /* Front */
  .card-front { left: 36px; width: 550px; background: var(--cream); }
  .floral-art {
    position: absolute; left: 12px; top: 4px; width: 526px; height: 440px;
    background: radial-gradient(ellipse at center, var(--violet-soft) 0%, var(--lilac) 55%, rgba(251,239,200,0) 75%);
  }
  .diamond { position: absolute; left: 0; top: 0; }
  .bird-art {
    position: absolute; left: 40px; top: 188px; width: 112px; height: 120px; border-radius: 50%;
    background: radial-gradient(circle, #8e3f86 0%, #b686c4 60%, rgba(183,134,196,0) 100%);
  }
  .front-copy { position: absolute; left: 117px; top: 110px; width: 330px; text-align: center; }
  .season-title { font-family: "Great Vibes", cursive; color: var(--plum); font-size: 40px; font-weight: 400; line-height: 44px; margin-bottom: 8px; }
  .front-copy p { font-size: 16.5px; line-height: 19px; }
  .front-copy .offer { margin-top: 5px; }
  .offer strong { color: var(--plum); font-weight: 700; }
  .front-phone { display: flex; align-items: center; justify-content: center; gap: 5px; color: var(--plum); font-weight: 700; font-size: 18px; line-height: 20px; margin-top: 5px; }
  .front-name { color: var(--plum); font-weight: 700; font-size: 18px; text-transform: uppercase; line-height: 22px; margin-top: 5px; }
  .front-brokerage { font-size: 16.5px; line-height: 20px; }

  /* Back */
  .card-back { left: 615px; width: 563px; background: var(--white); }
  .field-photo {
    position: absolute; left: 0; top: 0; width: 100%; height: 347px;
    background: linear-gradient(180deg, var(--sky) 0%, #f2f5f4 45%, #e3ece0 62%, var(--field) 75%, #f6e4f3 100%);
  }
  .agent-header { position: absolute; left: 33px; top: 32px; }
  .agent-name { font-weight: 700; color: var(--brand-blue); font-size: 30px; line-height: 32px; }
  .agent-tagline { color: var(--brand-blue); font-weight: 700; font-size: 11px; letter-spacing: .2px; }
  .brokerage-name { position: absolute; left: 236px; top: 42px; width: 96px; text-align: center; color: var(--brand-blue); font-weight: 700; font-size: 13px; line-height: 15px; }
  .return-address { position: absolute; left: 343px; top: 27px; font-family: "PT Sans Narrow", sans-serif; font-size: 13px; line-height: 15px; color: #333; font-style: normal; }
  .return-address .ra-name { color: var(--brand-blue); font-weight: 700; }
  .stamp-box { position: absolute; left: 463px; top: 27px; width: 63px; height: 61px; border: 2px solid var(--stamp); }

  .back-copy { position: absolute; left: 33px; top: 91px; width: 218px; font-family: "PT Sans Narrow", sans-serif; }
  .back-copy h2 { font-family: "Source Sans 3", sans-serif; color: var(--brand-blue); font-size: 17px; font-weight: 700; line-height: 22px; margin-bottom: 2px; }
  .back-copy p { font-size: 13px; line-height: 15.5px; margin-bottom: 5px; }
  .signature { position: absolute; left: 33px; top: 276px; font-family: "PT Sans Narrow", sans-serif; font-size: 14px; line-height: 16px; }
  .signature .sig-phone { display: flex; align-items: center; gap: 3px; color: var(--brand-blue); font-weight: 700; font-family: "Source Sans 3", sans-serif; font-size: 14px; }

  .barcode-zone { position: absolute; left: 0; top: 347px; width: 100%; height: 100px; background: var(--white); text-align: center; padding-top: 30px; font-family: "PT Sans Narrow", sans-serif; font-weight: 700; font-size: 14px; }
</style>
</head>
<body>

<section class="card card-front">
  <div class="floral-art" role="img" aria-label="Watercolour spring foliage in purple and lavender with small blue blossoms"></div>
  <svg class="diamond" width="550" height="447" viewBox="0 0 550 447" aria-hidden="true">
    <polygon points="282,20 520,216 282,412 44,216" fill="#ffffff"/>
    <polygon points="282,44 492,216 282,388 72,216" fill="none" stroke="var(--dash-blue)" stroke-width="1.6" stroke-dasharray="7 5"/>
  </svg>
  <div class="bird-art" role="img" aria-label="Watercolour songbird perched at the left edge of the diamond"></div>

  <div class="front-copy">
    <h1 class="season-title">Spring is Here</h1>
    <p>Homebuyers are beginning to look.<br>If you’re considering a move, Spring is<br>the best time to list your home!</p>
    <p class="offer">For a <strong>FREE</strong>, no-obligation market<br>analysis of your home, call today!</p>
    <div class="front-phone">
      <svg width="16" height="16" viewBox="0 0 16 16" aria-hidden="true"><circle cx="8" cy="8" r="7" fill="none" stroke="currentColor" stroke-width="1.3"/><path d="M5.5 4.5c.6-.3 1.1 0 1.3.5l.4 1c.1.4-.1.7-.4.9l-.4.3c.4 1 1.2 1.8 2.2 2.3l.3-.4c.2-.3.6-.5 1-.3l1 .5c.4.2.6.7.3 1.2-.5.8-1.4 1-2.3.6C7 10.4 5.5 8.8 4.9 6.9c-.3-.9 0-1.8.6-2.4z" fill="currentColor"/></svg>
      <span>(734) 555.0142</span>
    </div>
    <div class="front-name">Carl Whitby</div>
    <div class="front-brokerage">Harbor Key Realty</div>
  </div>
</section>

<section class="card card-back">
  <div class="field-photo" role="img" aria-label="Soft, faded landscape of a pink flower field under a pale sky"></div>

  <header class="agent-header">
    <div class="agent-name">Carl Whitby</div>
    <div class="agent-tagline">THE REAL ESTATE BUY (734) 555.0142</div>
  </header>
  <div class="brokerage-name">Harbor Key Realty</div>

  <address class="return-address">
    <div class="ra-name">CARL WHITBY</div>
    <div>7 Larkmoor Ct, Ste 240</div>
    <div>Riverbend, MI 48990</div>
  </address>
  <div class="stamp-box"></div>

  <article class="back-copy">
    <h2>A Track Record of Results!</h2>
    <p>When you list your home with me, I take the responsibility seriously. I will rpovide you with more than I promised everyday. My Service Guaranteeis based on more than a sale, it’s based on your complete happiness. There’s no question our market has slowed, but someone’s home will sell today. With the right Realtor, that home could your home.</p>
    <p>If you’re considering selling, call your neighborhood expert.</p>
  </article>

  <div class="signature">
    <div>Carl Whitby</div>
    <div class="sig-phone">
      <svg width="14" height="14" viewBox="0 0 16 16" aria-hidden="true"><circle cx="8" cy="8" r="7" fill="none" stroke="currentColor" stroke-width="1.3"/><path d="M5.5 4.5c.6-.3 1.1 0 1.3.5l.4 1c.1.4-.1.7-.4.9l-.4.3c.4 1 1.2 1.8 2.2 2.3l.3-.4c.2-.3.6-.5 1-.3l1 .5c.4.2.6.7.3 1.2-.5.8-1.4 1-2.3.6C7 10.4 5.5 8.8 4.9 6.9c-.3-.9 0-1.8.6-2.4z" fill="currentColor"/></svg>
      <span>(734) 555.0142</span>
    </div>
  </div>

  <div class="barcode-zone">USPS Bar Code Area</div>
</section>

</body>
</html>
```